この度は、たくさんのご提案をいただきまして、
誠にありがとうございました。
多くの素晴らしいデザインをご提案していただき、
本当に感謝しております。
今回、ご選考の結果、
ruto_artsさんのデザインを採用させていただきました。
※本案件に関しましては、書籍のイメージに一番合ったものが、
ruto_artsさんの表紙デザインだったため、
今回は、ruto_artsさんのご提案を選定させていただきました。
本当に、ありがとうございました。
また、今回は残念ながら、ご採用に至らなかった方も、
この度はお忙しいところ、本案件にご参加いただきまして、
今後も、継続的にお仕事をご発注させていただきますので、
また宜しければご参加いただければ幸いです。
以上、今後とも、何卒よろしくお願いいたします。
仕事は丁寧に進めていきたいと考えております。
もし、わからない点などがあれば、遠慮なく仰ってください。
1回切りのお仕事だけでなく、継続的にお仕事ができる方を探しております。

```html
<!DOCTYPE html>
<html lang="ja">
<head>
<meta charset="utf-8">
<title>普通の主婦の実体験記のすべて！</title>
<link rel="stylesheet" href="https://fonts.googleapis.com/css2?family=M+PLUS+Rounded+1c:wght@700;800;900&family=Noto+Sans+JP:wght@700;900&display=swap">
<style>
  :root {
    --paper: #ffffff;
    --ink: #1a1a1a;
    --orange: #f08a1c;
    --yellow: #ffe600;
    --magenta: #e6007e;
    --blue: #1d6fc4;
    --navy: #1456a8;
    --pink-bg: #ffe3ea;
    --red: #e60033;
    --accent-yellow: #fff100;
    --illust-top: #f6e9d8;
    --illust-bottom: #d9e8f5;
  }
  html, body { margin: 0; padding: 0; overflow: hidden; }
  body { width: 749px; height: 1200px; background: var(--paper); }
  .cover {
    position: relative; width: 749px; height: 1200px; overflow: hidden;
    background: var(--paper);
    font-family: "Noto Sans JP", sans-serif; color: var(--ink);
  }
  .banner {
    position: absolute; display: flex; flex-direction: column;
    align-items: center; justify-content: center;
    font-family: "M PLUS Rounded 1c", sans-serif; font-weight: 900;
    line-height: 1.12; text-align: center; box-sizing: border-box;
  }
  .banner--yellow {
    left: 360px; top: -50px; width: 440px; height: 230px;
    background: var(--yellow); color: var(--ink);
    transform: rotate(9deg); z-index: 1; padding: 40px 40px 0 0;
  }
  .banner--yellow .banner-lead { font-size: 48px; }
  .banner--yellow .banner-main { font-size: 44px; }
  .banner--orange {
    left: -40px; top: -45px; width: 430px; height: 230px;
    background: var(--orange); color: #fff;
    transform: rotate(-9deg); z-index: 2; padding: 45px 0 0 30px;
  }
  .banner--orange .banner-lead { font-size: 48px; }
  .banner--orange .banner-main { font-size: 46px; }

  .subtitle {
    position: absolute; top: 212px; left: 0; width: 749px; margin: 0;
    text-align: center; line-height: 1;
    font-size: 58px; font-weight: 900; letter-spacing: 1px; z-index: 3;
  }
  .title {
    position: absolute; top: 262px; left: 0; width: 749px; margin: 0;
    text-align: center; font-size: 150px; font-weight: 900; line-height: 1;
    letter-spacing: 2px; z-index: 3;
    text-shadow: 6px 6px 0 rgba(0,0,0,0.2);
  }
  .title-first { color: var(--magenta); }
  .title-rest { color: var(--blue); }
  .title-tail {
    position: absolute; top: 400px; right: 38px; line-height: 1.2;
    font-size: 48px; font-weight: 900; z-index: 3;
  }

  .callout {
    position: absolute; left: 13px; top: 470px; width: 224px; height: 226px;
    background: var(--pink-bg); border: 4px solid var(--red); border-radius: 20px;
    box-sizing: border-box; color: var(--red); text-align: center;
    font-family: "M PLUS Rounded 1c", sans-serif; font-weight: 900;
    display: flex; flex-direction: column; justify-content: center; z-index: 3;
  }
  .callout-head { font-size: 42px; line-height: 1.15; }
  .callout-body { font-size: 25px; line-height: 1.3; margin-top: 8px; }

  .illustration {
    position: absolute; left: 244px; top: 462px; width: 466px; height: 310px;
    background: linear-gradient(160deg, var(--illust-top), var(--illust-bottom));
    border-radius: 16px; z-index: 2;
  }

  .author {
    position: absolute; right: 24px; top: 776px; line-height: 1.2;
    font-size: 36px; font-weight: 700; z-index: 3;
  }

  .blurb {
    position: absolute; left: 0; top: 828px; width: 749px; height: 372px;
    background: var(--navy); box-sizing: border-box; padding: 34px 30px;
    color: #fff; font-size: 37px; font-weight: 700; line-height: 1.6;
  }
  .blurb p { margin: 0; }
  .highlight { color: var(--accent-yellow); }
  .highlight--boxed { background: var(--red); color: var(--accent-yellow); padding: 0 2px; }
</style>
</head>
<body>
<main class="cover">
  <div class="banner banner--yellow">
    <span class="banner-lead">0円で</span>
    <span class="banner-main">さよなら花粉症</span>
  </div>
  <div class="banner banner--orange">
    <span class="banner-lead">0円で</span>
    <span class="banner-main">便秘よさらば</span>
  </div>

  <h2 class="subtitle">普通の主婦の</h2>
  <h1 class="title"><span class="title-first">実</span><span class="title-rest">体験記</span></h1>
  <div class="title-tail">のすべて！</div>

  <div class="callout">
    <div class="callout-head">ひと月で<br>実感！</div>
    <div class="callout-body">バナナ便スルスル<br>忘れた花粉症</div>
  </div>

  <div class="illustration" role="img" aria-label="笑顔で両手を上げて喜ぶ主婦と、トイレのドアのイラスト"></div>

  <div class="author">オフィス三田村</div>

  <section class="blurb">
    <p>普通の主婦が、誰の助けも得ず、毎日の生活を変えることなく、長年悩まされた<span class="highlight--boxed">「便秘」</span>と<span class="highlight--boxed">「花粉症」</span>の悩みを、なんと<span class="highlight">1円も使わず0円でついに解決！</span></p>
  </section>
</main>
</body>
</html>
```